Banner Ad Design Project

I need a banner design. The website is under construction at www.brightmarrowfield.com

Name: Bright Marrow
Tagline: Leadership Inspiration for busy people

This is a leadership development and executive coaching site. The past site is live at www.quillponderhub.com. (so you can get a sense of the content)

The audience are (BUSY) executives, senior managers, leaders and top professionals, so the feel needs to be highly professional but also modern and fresh. I want to communicate energy but also solid and trust worthy and not too new agey. The audience are also people with strong social values who want to change things - so not too corporate (Ie suits!)

I would like the design to be floating on a white background, very clean and simple. I am attracted to reds or sunset (burn orange crimson colors.) But totally open to any color ideas.
I am giving an open brief for your ideas.
Here are the dimensions 960px wide, roughly 190px height.
Updates

Project Deadline Extended
Reason: The weekend might give more time to designers to get involved. Thanks Mirel

Hi designers

You may not have seen the additions I gave to this brief.

The banner should not have leader out front photo's. Maybe less corporate than I initially thought. 
Not too corporate (no suits!) Please no chess pieces, jigsaw pieces, cartoon images, cliche leadership images. 
Am am trying for inspiration /inspiring whilst still being professional. Very simple and clean.
Please can the design be floating in a white background so that the web page is borderless - A bit like it is in http://tamberwickcove.com/
Thank you

Target Market(s)

Senior managers, executives but people who also want to change the world!

Industry/Entity Type

Construction

Requirements
Should not have
• Should not have leader out front photo's.
Maybe less corporate than I initially thought.
Am am trying for inspiration /inspiring whilst still being professional.
Please no chess pieces, jigsaw pieces, cartoon images, cliche leadership images. Not too corporate (Ie suits!)

Thanks

```html
<!DOCTYPE html>
<html lang="en">
<head>
<meta charset="utf-8">
<title>Bright Marrow — Banner</title>
<link rel="stylesheet" href="https://fonts.googleapis.com/css2?family=Mulish:wght@400;800&family=Questrial&display=swap">
<style>
  :root {
    --coral: #ea4a38;
    --orange: #ee5a35;
    --crimson: #a8182d;
    --band-top: #f2b8b5;
    --band-mid: #f9dedc;
    --paper: #ffffff;
    --globe-light: #8cc3ea;
    --globe-deep: #1f6aa8;
  }
  html, body {
    margin: 0;
    padding: 0;
    overflow: hidden;
    background: var(--paper);
  }
  .banner {
    position: relative;
    width: 1200px;
    height: 238px;
    overflow: hidden;
    background: var(--paper);
    font-family: "Mulish", "Helvetica Neue", Arial, sans-serif;
  }
  .banner__band {
    position: absolute;
    left: 0;
    right: 0;
    top: 206px;
    height: 32px;
    background: linear-gradient(to bottom, var(--band-top) 0%, var(--band-mid) 30%, var(--paper) 100%);
  }
  .headline {
    position: absolute;
    left: 82px;
    top: 46px;
    margin: 0;
    font-weight: 400;
  }
  .headline__lead {
    display: block;
    font-size: 28px;
    line-height: 1;
    color: var(--orange);
    white-space: nowrap;
  }
  .headline__lead strong {
    color: var(--crimson);
    font-weight: 800;
  }
  .headline__title {
    display: block;
    margin-top: 3px;
    font-family: "Questrial", "Century Gothic", sans-serif;
    font-weight: 400;
    font-size: 103px;
    line-height: 1;
    color: var(--coral);
    letter-spacing: -0.5px;
    white-space: nowrap;
  }
  .promise {
    position: absolute;
    left: 767px;
    top: 58px;
    margin: 0;
    font-size: 28px;
    line-height: 34px;
    color: var(--orange);
    white-space: nowrap;
  }
  .promise strong {
    color: var(--crimson);
    font-weight: 800;
  }
  .globe-art {
    position: absolute;
    left: 1070px;
    top: 96px;
    width: 120px;
    height: 100px;
    border-radius: 10px;
    background: linear-gradient(135deg, var(--globe-light), var(--globe-deep));
  }
</style>
</head>
<body>
  <div class="banner">
    <div class="banner__band"></div>

    <h1 class="headline">
      <span class="headline__lead">What to <strong>do</strong> when <strong>you</strong> dont <strong>know</strong> what to do!</span>
      <span class="headline__title">Bright Marrow</span>
    </h1>

    <p class="promise">
      <strong>Leading</strong> big and Small<br>
      <strong>Change</strong> at<br>
      Work and <strong>in Life</strong>
    </p>

    <div class="globe-art" role="img" aria-label="Illustration area: a blue globe with an orange arrow sweeping around it"></div>
  </div>
</body>
</html>
```